Life Coach for Lawyers Business Card Design

Elegant, original, business card design for life coaching service for associate attorneys who work in big law and struggle with stress, overwhelm, and time management. Double sided design.

Target Market(s)

Women associate attorneys who work in big law and struggle with stress, overwhelm, and time management.

Industry/Entity Type

Life Coaching

Contact Information for Business Card

Marissa Pendrell
Life Coach
518.677.3941
calmbriefcounsel.net
marissa@calmbriefcounsel.net
@calmbriefcounsel (Instagram)

Font styles to use
Other font styles liked:
• Silver South font duo. See uploaded files.

Requirements
Must have
• Icons for phone, website, email, and Instagram instead of words. Specific colors used in my logo (171B2B, 421121, FFFFFF)
Nice to have
• Foil. Embossed. Feminine design.
Should not have
• Any colors other than those used in logo. See uploaded files.

```html
<!DOCTYPE html>
<html lang="en">
<head>
<meta charset="utf-8">
<title>Calm Brief Counsel – Business Card</title>
<link href="https://fonts.googleapis.com/css2?family=Playfair+Display:wght@400&family=Allura&display=swap" rel="stylesheet">
<style>
  :root {
    --navy: #171B2B;
    --maroon: #421121;
    --white: #FFFFFF;
    --page: #FFFFFF;
  }
  html, body {
    margin: 0;
    padding: 0;
    width: 1200px;
    height: 1200px;
    overflow: hidden;
    background: var(--page);
  }
  .canvas {
    position: relative;
    width: 1200px;
    height: 1200px;
  }
  .card {
    position: absolute;
    left: 130px;
    width: 922px;
    height: 441px;
    overflow: hidden;
    background: var(--navy);
  }
  .card--front { top: 78px; }
  .card--back { top: 650px; }
  .card__shapes {
    position: absolute;
    inset: 0;
    width: 100%;
    height: 100%;
  }
  .brand {
    position: absolute;
    color: var(--white);
    font-family: "Playfair Display", serif;
    font-weight: 400;
    text-transform: uppercase;
    text-align: center;
    line-height: 1;
    margin: 0;
  }
  .brand--front {
    left: 162px;
    top: 110px;
    width: 568px;
    height: 181px;
    display: flex;
    flex-direction: column;
    justify-content: center;
    font-size: 56px;
    letter-spacing: 4px;
  }
  .brand--back {
    left: 167px;
    top: 222px;
    width: 300px;
    transform: translate(-50%, -50%) rotate(-90deg);
    font-size: 40px;
    letter-spacing: 3px;
  }
  .identity {
    position: absolute;
    left: 520px;
    top: 62px;
    width: 330px;
    color: var(--white);
    font-family: "Allura", cursive;
    text-align: right;
  }
  .identity__name {
    font-size: 44px;
    line-height: 1;
    margin: 0;
    border-bottom: 1px solid var(--white);
    padding-bottom: 2px;
  }
  .identity__title {
    font-size: 28px;
    line-height: 1.1;
    margin: 2px 0 0;
  }
  .contacts {
    position: absolute;
    right: 0;
    top: 198px;
    margin: 0;
    padding: 0;
    list-style: none;
  }
  .contact {
    display: flex;
    align-items: center;
    justify-content: flex-end;
    height: 30px;
    margin-bottom: 13px;
  }
  .contact__text {
    color: var(--white);
    font-family: "Allura", cursive;
    font-size: 25px;
    margin-right: 12px;
    white-space: nowrap;
  }
  .contact__pill {
    width: 122px;
    height: 30px;
    background: var(--navy);
    border-radius: 15px 0 0 15px;
    display: flex;
    align-items: center;
    padding-left: 18px;
    box-sizing: border-box;
  }
  .contact__icon {
    width: 20px;
    height: 20px;
  }
</style>
</head>
<body>
<div class="canvas">

  <section class="card card--front" aria-label="Card front">
    <svg class="card__shapes" viewBox="0 0 1152 551" preserveAspectRatio="none" aria-hidden="true">
      <polygon fill="#421121" points="685,0 1152,0 1152,392 912,198 912,138 850,138"/>
      <polygon fill="#421121" points="0,138 202,265 202,364 313,364 535,551 0,551"/>
      <rect fill="#421121" x="202" y="138" width="710" height="226"/>
    </svg>
    <h1 class="brand brand--front"><span>Calm Brief</span><span>Counsel</span></h1>
  </section>

  <section class="card card--back" aria-label="Card back">
    <svg class="card__shapes" viewBox="0 0 1152 552" preserveAspectRatio="none" aria-hidden="true">
      <polygon fill="#421121" points="710,0 1152,0 1152,552 645,552 422,288"/>
    </svg>
    <p class="brand brand--back">Calm Brief<br>Counsel</p>

    <div class="identity">
      <p class="identity__name">Marissa Pendrell</p>
      <p class="identity__title">Life Coach</p>
    </div>

    <ul class="contacts">
      <li class="contact">
        <span class="contact__text">518.677.3941</span>
        <span class="contact__pill">
          <svg class="contact__icon" viewBox="0 0 24 24" fill="none" stroke="#FFFFFF" stroke-width="1.6" stroke-linejoin="round" aria-label="Phone">
            <path d="M5 3h4l2 5-2.5 1.5a11 11 0 0 0 6 6L16 13l5 2v4a2 2 0 0 1-2 2A16 16 0 0 1 3 5a2 2 0 0 1 2-2z"/>
          </svg>
        </span>
      </li>
      <li class="contact">
        <span class="contact__text">marissa@calmbriefcounsel.net</span>
        <span class="contact__pill">
          <svg class="contact__icon" viewBox="0 0 24 24" aria-label="Email">
            <rect x="2" y="5" width="20" height="14" fill="#FFFFFF"/>
            <path d="M2 5l10 8 10-8" fill="none" stroke="#171B2B" stroke-width="1.6"/>
          </svg>
        </span>
      </li>
      <li class="contact">
        <span class="contact__text">@calmbriefcounsel</span>
        <span class="contact__pill">
          <svg class="contact__icon" viewBox="0 0 24 24" aria-label="Social handle">
            <circle cx="12" cy="12" r="8" fill="none" stroke="#FFFFFF" stroke-width="2"/>
          </svg>
        </span>
      </li>
      <li class="contact">
        <span class="contact__text">calmbriefcounsel.net</span>
        <span class="contact__pill">
          <svg class="contact__icon" viewBox="0 0 24 24" fill="none" stroke="#FFFFFF" stroke-width="1.5" aria-label="Website">
            <circle cx="12" cy="12" r="9" fill="#FFFFFF" stroke="none"/>
            <ellipse cx="12" cy="12" rx="4" ry="9" stroke="#171B2B"/>
            <path d="M3 12h18M5 7h14M5 17h14" stroke="#171B2B"/>
          </svg>
        </span>
      </li>
    </ul>
  </section>

</div>
</body>
</html>
```